To revamp the exting web page and Company presentation to new propsective client

We are company establish in 2006. We have a combine of Veltra implementation team of more than 10 years. We focus on the following areas

a) Veltra Nimbus suite implementation
b) Veltra Nimbus suite platform migration
c) Large database size in excess of 20TB

We need to redesign a our existing new card to give a new look and refresh look. Kindly visit our website for more info www.halvtek.com

Your main them is blue color and hope to hear from you all.

Target Market(s)

Professional clients

Industry/Entity Type

Information Technology

Contact Information for Business Card

To market our as the leading Veltra partner in Veltra nimbus suite implementation

Number of Pages Required

1 page

Colors
3276b5
9bcb3c
cadf82
33a6d7

Requirements
Must have
• The ability to attract new customer and show a level of professionalism.
• You can also add a green color to represent green and environmental friendly.
Nice to have
• To give a total new fresh look for the company
Should not have
• None

```html
<!DOCTYPE html>
<html lang="en">
<head>
<meta charset="utf-8">
<title>Halvtek Business Card</title>
<link rel="stylesheet" href="https://fonts.googleapis.com/css2?family=Carlito:wght@400;700&display=swap">
<style>
  :root {
    --navy: #252a6b;
    --ink: #3b3f4a;
    --muted: #4a4f5c;
    --bg: #e4e6ea;
    --blue-a: #245a8c;
    --blue-b: #35308a;
    --blue-c: #2a6290;
    --paper-a: #ffffff;
    --paper-b: #eceef0;
  }
  * { box-sizing: border-box; margin: 0; padding: 0; }
  html, body { width: 1200px; height: 1200px; overflow: hidden; }
  body {
    background: var(--bg);
    font-family: "Carlito", "Calibri", sans-serif;
    display: flex;
    flex-direction: column;
    align-items: center;
    justify-content: center;
    gap: 80px;
  }
  .card {
    width: 700px;
    height: 400px;
    position: relative;
    box-shadow: 0 6px 18px rgba(0,0,0,0.18);
  }
  .card-front {
    background: linear-gradient(90deg, var(--blue-a) 0%, var(--blue-b) 22%, var(--blue-c) 45%, var(--blue-b) 70%, var(--blue-a) 100%);
    display: flex;
    align-items: center;
    justify-content: center;
  }
  .front-name {
    color: #ffffff;
    font-weight: 700;
    font-size: 64px;
    letter-spacing: 14px;
  }
  .card-back {
    background: linear-gradient(100deg, var(--paper-a) 0%, var(--paper-b) 35%, var(--paper-a) 60%, var(--paper-b) 100%);
  }
  .back-logo {
    position: absolute;
    left: 44px;
    top: 100px;
    display: flex;
    align-items: center;
    gap: 10px;
  }
  .logo-dot {
    width: 26px; height: 26px;
    border-radius: 50%;
    background: var(--navy);
  }
  .logo-name {
    color: var(--navy);
    font-weight: 700;
    font-size: 36px;
    letter-spacing: 8px;
  }
  .person {
    position: absolute;
    left: 410px;
    top: 34px;
  }
  .person-name {
    color: var(--navy);
    font-weight: 700;
    font-size: 28px;
  }
  .person-title {
    color: var(--muted);
    font-size: 15px;
    margin-top: 4px;
    margin-left: 20px;
  }
  .contact {
    position: absolute;
    left: 410px;
    color: var(--ink);
    font-size: 16px;
    line-height: 22px;
  }
  .contact-main { top: 120px; }
  .contact-extra { top: 200px; }
  .contact-rule {
    position: absolute;
    left: 400px;
    right: 36px;
    top: 188px;
    border-top: 1px solid var(--navy);
  }
  .address {
    position: absolute;
    left: 44px;
    top: 176px;
    color: var(--muted);
    font-size: 17px;
    line-height: 24px;
  }
  .divider {
    position: absolute;
    left: 44px;
    right: 36px;
    top: 290px;
    border-top: 1px solid var(--navy);
  }
  .website {
    position: absolute;
    left: 44px;
    top: 305px;
    color: var(--navy);
    font-size: 44px;
  }
</style>
</head>
<body>
  <section class="card card-front">
    <div class="front-name">HALVTEK</div>
  </section>

  <section class="card card-back">
    <div class="back-logo">
      <span class="logo-dot"></span>
      <span class="logo-name">HALVTEK</span>
    </div>

    <div class="person">
      <div class="person-name">DARREN KOH</div>
      <div class="person-title">Chief Operating Officer</div>
    </div>

    <div class="contact contact-main">
      <div>M : 60 12 418 5520</div>
      <div>T : 603 - 7731 5064</div>
      <div>E : darrenkoh@halvtek.com</div>
    </div>
    <div class="contact-rule"></div>
    <div class="contact contact-extra">
      <div>F : 603 - 7731 5090</div>
      <div>T : 65 6274 3918 (Singapore)</div>
    </div>

    <address class="address" style="font-style: normal;">
      Suite 5.02, 5th Floor<br>
      Menara Selatan, Riverside Park<br>
      Jalan Cempaka Indah<br>
      58100 Kuala Lumpur, Malaysia
    </address>

    <div class="divider"></div>
    <div class="website">www.halvtek.com</div>
  </section>
</body>
</html>
```